Webdesign (Portalskonzept und -design) für Online-Portal
Zielgruppe
Mit KOMPASS (www.kompassonline-beispiel.ch) besteht ein starker Brand in der Ostschweiz für ein Magazin, dass monatlich an über 8'000 CEO’s (Kader) der Ostschweiz per Post versendet wird. Aktuelle News sind auf dem Portal von KOMPASS online aufgeschaltet und werden via Newsletter versendet. Der Brand KOMPASS ist in der Ostschweiz bekannt und etabliert. Nun soll der Offline-Brand für die digitale Zukunft gerüstet werden.
Aufgabenstellung
Entwicklung modernes Portaldesign (Webseite) in responsive / mobile first => www.kompassdigital-beispiel.ch
Ziel; Es soll ein Online-Portal unter dem Brand kompassdigital-beispiel.ch aufgebaut werden. Auf diesem Portal integriert werden die News (kompassonline-beispiel.ch) sowie weitere Unterrubriken wie z.B. Jobs, Events, etc.
Beispiel: KOMPASStalk, KOMPASSjobs, KOMPASSevent, etc.
Der bestehende Brand KOMPASS (offline) muss dabei zwingender Bestandteil zur Wiedererkennung sein und darf nicht verändert sondern nur ergänzt werden. Das Portal kann man sich vorstellen wie vergleichzone-beispiel.de – eine laufende Erweiterung um weitere Rubriken soll möglich sein. Der Brand / das Logo darf für KOMPASSDigital 'erweitert' werden.
Das Design soll modern & schlank wirken sowie primär für Mobilgeräte (mobile first) gestaltet sein.
Bei http://www.medinetz-plattform-beispiel.de/index.php finden wir die 2. Navigations-Ebene interessant umgesetzt. Mit besseren Symbolen könnte das eine gute Art sein.
Vom Look & Feel gefällt https://www.wirtschaftsblick-beispiel.ch (Startseite für News)

```html
<!DOCTYPE html>
<html lang="de">
<head>
<meta charset="utf-8">
<title>KOMPASSDIGITAL – Das Unternehmermagazin</title>
<link href="https://fonts.googleapis.com/css2?family=Lato:ital,wght@0,400;0,700;0,900;1,400&display=swap" rel="stylesheet">
<style>
:root{
  --red:#9b1c1f;
  --red-dark:#7d0f12;
  --text:#333;
  --muted:#555;
  --light:#f1f1f1;
  --line:#ddd;
  --footer:#3b3b3b;
  --white:#fff;
}
*{box-sizing:border-box;margin:0;padding:0}
html,body{width:1200px;height:3348px;overflow:hidden}
body{position:relative;font-family:'Lato',sans-serif;color:var(--text);background:var(--white)}
.abs{position:absolute}
a{color:inherit;text-decoration:none}

.topbar{left:0;top:0;width:1200px;height:29px;background:var(--red-dark);color:var(--white);font-size:11px}
.topbar .item{position:absolute;top:8px;display:flex;align-items:center;gap:5px}
.topbar svg{width:13px;height:13px;fill:none;stroke:var(--white);stroke-width:2}

.masthead{left:0;top:29px;width:1200px;height:89px;background:var(--red)}
.brand{position:absolute;left:231px;top:10px;color:var(--white)}
.brand .name{font-size:54px;font-weight:400;letter-spacing:1px;line-height:56px}
.brand .claim{font-size:12px;font-weight:700;letter-spacing:.6px;margin-top:-2px}

.mainnav{left:0;top:118px;width:1200px;height:34px;border-bottom:1px solid var(--line);font-size:14px;font-style:italic}
.mainnav .item{position:absolute;top:8px}
.mainnav .active{color:var(--red)}
.mainnav .more{font-style:normal;display:flex;align-items:center;gap:10px}

.hero-img{left:0;top:157px;width:1200px;height:406px;background:linear-gradient(135deg,#5d5a56,#a4876a 45%,#c8a985 60%,#5e5b58)}
.hero-card{left:231px;top:497px;width:736px;height:211px;background:var(--white);border-top:4px solid var(--red);padding:12px 13px}
.hero-card .cat{color:var(--red);font-size:16px}
.hero-card h1{font-size:25px;font-weight:400;margin:2px 0 14px}
.lead{font-size:11.5px;line-height:19px;color:var(--muted)}
.btn{display:inline-block;background:var(--red);color:var(--white);font-size:12px;font-weight:700;text-align:center}
.hero-card .btn{position:absolute;right:13px;top:156px;width:220px;height:31px;line-height:31px}

.searchband{left:0;top:747px;width:1200px;height:112px;background:var(--light)}
.field{position:absolute;top:37px;height:38px;background:var(--white);border:1px solid var(--line);font-size:12px;padding:0 13px;line-height:36px}
.field.input{left:231px;width:359px;font-style:italic;color:#777}
.field.select{left:608px;width:296px;color:var(--text)}
.field.select svg{position:absolute;right:12px;top:14px}
.search-go{position:absolute;left:923px;top:37px;width:44px;height:38px;background:var(--red);display:flex;align-items:center;justify-content:center}

.card{width:233px;height:306px;background:var(--white);box-shadow:0 1px 5px rgba(0,0,0,.22);border-bottom:3px solid var(--red)}
.card .media{height:151px}
.card .body{padding:14px 13px 0}
.card .cat{color:var(--red);font-size:10px;font-weight:900}
.card h3{font-size:15px;font-weight:900;line-height:19px;margin:2px 0 6px}
.card p{font-size:11.5px;line-height:17.5px;color:var(--muted)}
.more-link{color:var(--red);font-weight:700}
.ad{width:233px;height:306px;background:var(--light)}
.ad .slot{position:absolute;left:10px;top:65px;width:212px;height:176px;background:#a9a9a9;color:var(--white);font-size:12px;display:flex;align-items:center;justify-content:center}

.feature{left:231px;top:1634px;width:736px;height:430px;background:var(--white);box-shadow:0 1px 5px rgba(0,0,0,.22);border-bottom:3px solid var(--red)}
.feature .media{height:271px;background:linear-gradient(180deg,#6d9a86,#3e5f63 60%,#2b3b55)}
.feature .body{padding:14px 13px}
.feature .cat{color:var(--red);font-size:16px}
.feature h2{font-size:25px;font-weight:400;margin:2px 0 14px}

.aboband{left:0;top:2514px;width:1200px;height:213px;background:var(--light)}
.abo-text{position:absolute;left:231px;top:27px;width:470px}
.abo-text .cat{color:var(--red);font-size:10px;font-weight:900}
.abo-text h2{font-size:22px;font-weight:900;line-height:25px;color:#444;margin:4px 0 8px}
.abo-text p{font-size:11.5px;line-height:17.5px;color:var(--muted)}
.abo-text .btn{margin-top:15px;width:171px;height:30px;line-height:30px}
.magazine{left:737px;top:2535px;width:128px;height:169px;background:linear-gradient(160deg,#2e2e2e,#6b2024 55%,#9c9ca0);box-shadow:2px 3px 5px rgba(0,0,0,.35);transform:rotate(4deg)}

.footer{left:0;top:3141px;width:1200px;height:207px;background:var(--footer);color:var(--white)}
.rubrics{position:absolute;left:231px;top:32px;width:736px;display:grid;grid-template-columns:repeat(5,1fr);border:1px solid #8a8a8a}
.rubrics span{height:44px;display:flex;align-items:center;justify-content:center;font-size:12.5px;letter-spacing:.3px;border-right:1px solid #8a8a8a;border-bottom:1px solid #8a8a8a}
.rubrics span:nth-child(5n){border-right:0}
.rubrics span:nth-child(n+6){border-bottom:0}
.footlinks{position:absolute;left:0;width:1200px;top:146px;text-align:center;font-size:12px}
.copyright{position:absolute;left:0;width:1200px;top:172px;text-align:center;font-size:12px}
</style>
</head>
<body>

<div class="abs topbar">
  <div class="item" style="left:686px"><svg viewBox="0 0 24 24"><path d="M5 3h4l2 5-3 2a12 12 0 0 0 6 6l2-3 5 2v4a2 2 0 0 1-2 2A17 17 0 0 1 3 5a2 2 0 0 1 2-2z"/></svg>+41 (0)71 000 12 34</div>
  <div class="item" style="left:835px"><svg viewBox="0 0 24 24"><rect x="3" y="5" width="18" height="14" fill="#fff" stroke="none"/><path d="M3 6l9 7 9-7" stroke="#7d0f12"/></svg></div>
  <div class="item" style="left:876px"><svg viewBox="0 0 24 24"><circle cx="10" cy="10" r="6"/><path d="M15 15l6 6"/></svg></div>
  <div class="item" style="left:918px"><svg viewBox="0 0 24 24"><circle cx="12" cy="12" r="9"/><circle cx="12" cy="10" r="3"/><path d="M6 18c2-3 10-3 12 0"/></svg>Login</div>
</div>

<header class="abs masthead">
  <div class="brand">
    <div class="name">KOMPASSDIGITAL</div>
    <div class="claim">DAS UNTERNEHMERMAGAZIN</div>
  </div>
</header>

<nav class="abs mainnav">
  <span class="item" style="left:232px;top:10px"><svg width="14" height="12" viewBox="0 0 14 12"><path d="M7 0L0 6h2v6h4V8h2v4h4V6h2z" fill="#333"/></svg></span>
  <a class="item active" style="left:280px">•NEWS</a>
  <a class="item" style="left:365px">•EVENTS</a>
  <a class="item" style="left:461px">•JOBS</a>
  <a class="item" style="left:541px">•TALK</a>
  <a class="item" style="left:619px">•FINANZEN</a>
  <a class="item" style="left:732px">•IMMOBILIEN</a>
  <a class="item more" style="left:900px">mehr <svg width="24" height="14" viewBox="0 0 24 14"><path d="M0 1h24M0 7h24M0 13h24" stroke="#333" stroke-width="2"/></svg></a>
</nav>

<div class="abs hero-img" role="img" aria-label="Foto: Reiseführer-Broschüren aus Kraftpapier auf dunklem Holztisch"></div>
<article class="abs hero-card">
  <div class="cat">REISEN</div>
  <h1>Nullam dictum felis eu pede mollis pretium.</h1>
  <p class="lead">Lorem ipsum dolor sit amet, consectetuer adipiscing elit. Aenean commodo ligula eget dolor. Aenean massa. Cum sociis natoque penatibus et magnis dis parturient montes, nascetur ridiculus mus. Donec quam felis, ultricies nec, pellentesque eu, pretium qui, sem. Nulla consequat massa quis enim. Donec pede justo, fringilla vel, aliquet nec, vulputate eget, arcu. Donec pede justo, fringilla vel, ...</p>
  <a class="btn">weiterlesen</a>
</article>

<section class="abs searchband">
  <div class="field input">Suchbegriff eingeben</div>
  <div class="field select">Alle News<svg width="9" height="6" viewBox="0 0 9 6"><path d="M1 1l3.5 3.5L8 1" stroke="#333" fill="none" stroke-width="1.4"/></svg></div>
  <div class="search-go"><svg width="12" height="18" viewBox="0 0 12 18"><path d="M2 2l7 7-7 7" stroke="#fff" stroke-width="2.5" fill="none"/></svg></div>
</section>

<!-- Row 1 -->
<article class="abs card" style="left:231px;top:923px"><div class="media" role="img" aria-label="Foto: Hausfassade mit Hecke" style="background:linear-gradient(180deg,#c9c2b8,#b9a999 55%,#3f6a2a)"></div><div class="body"><div class="cat">REGIONAL</div><h3>Lorem ipsum dolor sit amet, consectetuer adipiscing elit.</h3><p>Aenean commodo ligula eget dolor. Aenean massa. Cum sociis natoque penatibus et magnis dis parturient montes, nascetur ridiculus... | <span class="more-link">mehr</span></p></div></article>
<article class="abs card" style="left:482px;top:923px"><div class="media" role="img" aria-label="Foto: Golfplatz mit Fahne vor Bergkulisse" style="background:linear-gradient(180deg,#9cc2e0,#c9d8e4 30%,#4e7a35 50%,#7fb236)"></div><div class="body"><div class="cat">SPORT</div><h3>Lorem ipsum dolor sit amet, consectetuer adipiscing elit.</h3><p>Aenean commodo ligula eget dolor. Aenean massa. Cum sociis natoque penatibus et magnis dis parturient montes, nascetur ridiculus... | <span class="more-link">mehr</span></p></div></article>
<article class="abs card" style="left:734px;top:923px"><div class="media" role="img" aria-label="Foto: helles Hotelzimmer mit Bett" style="background:linear-gradient(180deg,#d8d2c8,#b8a58e 60%,#e6e1da)"></div><div class="body"><div class="cat">REISEN</div><h3>Lorem ipsum dolor sit amet, consectetuer adipiscing elit.</h3><p>Aenean commodo ligula eget dolor. Aenean massa. Cum sociis natoque penatibus et magnis dis parturient montes, nascetur ridiculus... | <span class="more-link">mehr</span></p></div></article>

<!-- Row 2 -->
<article class="abs card" style="left:231px;top:1251px"><div class="media" role="img" aria-label="Porträtfoto einer Person vor weissem Hintergrund" style="background:linear-gradient(180deg,#f6f6f6,#e2d6c8 70%,#2c2c2c)"></div><div class="body"><div class="cat">REGIONAL</div><h3>Lorem ipsum dolor sit amet, consectetuer adipiscing elit.</h3><p>Aenean commodo ligula eget dolor. Aenean massa. Cum sociis natoque penatibus et magnis dis parturient montes, nascetur ridiculus... | <span class="more-link">mehr</span></p></div></article>
<article class="abs card" style="left:482px;top:1251px"><div class="media" role="img" aria-label="Foto: Firmenschild einer Webagentur" style="background:linear-gradient(180deg,#e8e8ec,#c7c8d4)"></div><div class="body"><div class="cat">TECHNOLOGY</div><h3>Lorem ipsum dolor sit amet, consectetuer adipiscing elit.</h3><p>Aenean commodo ligula eget dolor. Aenean massa. Cum sociis natoque penatibus et magnis dis parturient montes, nascetur ridiculus... | <span class="more-link">mehr</span></p></div></article>
<aside class="abs ad" style="left:734px;top:1251px"><div class="slot">Anzeige</div></aside>

<!-- Feature -->
<article class="abs feature">
  <div class="media" role="img" aria-label="Foto: drei Männer in Anzügen auf einer Stadiontribüne"></div>
  <div class="body">
    <div class="cat">TECHNOLOGY</div>
    <h2>Nullam dictum felis eu pede mollis pretium</h2>
    <p class="lead">Lorem ipsum dolor sit amet, consectetuer adipiscing elit. Aenean commodo ligula eget dolor. Aenean massa. Cum sociis natoque penatibus et magnis dis parturient montes, nascetur ridiculus mus. Donec quam felis, ultricies nec, pellentesque eu, pretium qui, sem. Nulla consequat massa quis enim. Donec pede justo, fringilla vel, aliquet nec, vulputate eget, arcu. Donec pede justo... | <span class="more-link">mehr</span></p>
  </div>
</article>

<!-- Row 3 -->
<article class="abs card" style="left:231px;top:2142px"><div class="media" role="img" aria-label="Foto: Kathedrale mit Zuschauern auf dem Platz" style="background:linear-gradient(180deg,#c6d3e0,#a79a86 50%,#3b3a36)"></div><div class="body"><div class="cat">REGIONAL</div><h3>Lorem ipsum dolor sit amet, consectetuer adipiscing elit.</h3><p>Aenean commodo ligula eget dolor. Aenean massa. Cum sociis natoque penatibus et magnis dis parturient montes, nascetur ridiculus... | <span class="more-link">mehr</span></p></div></article>
<article class="abs card" style="left:482px;top:2142px"><div class="media" role="img" aria-label="Porträtfoto einer Person vor gelber Wand" style="background:linear-gradient(180deg,#f2d63e,#e8c52f 60%,#3a3a3a)"></div><div class="body"><div class="cat">WIRTSCHAFT</div><h3>Lorem ipsum dolor sit amet, consectetuer adipiscing elit.</h3><p>Aenean commodo ligula eget dolor. Aenean massa. Cum sociis natoque penatibus et magnis dis parturient montes, nascetur ridiculus... | <span class="more-link">mehr</span></p></div></article>
<article class="abs card" style="left:734px;top:2142px"><div class="media" role="img" aria-label="Foto: drei Männer vor einem Firmenschild" style="background:linear-gradient(180deg,#3d4046,#6a6e74 45%,#1f2228)"></div><div class="body"><div class="cat">WIRTSCHAFT</div><h3>Lorem ipsum dolor sit amet, consectetuer adipiscing elit.</h3><p>Aenean commodo ligula eget dolor. Aenean massa. Cum sociis natoque penatibus et magnis dis parturient montes, nascetur ridiculus... | <span class="more-link">mehr</span></p></div></article>

<!-- Abo -->
<section class="abs aboband">
  <div class="abo-text">
    <div class="cat">ABONNIEREN</div>
    <h2>Lorem ipsum dolor sit amet, consectetuer adipiscing elit.</h2>
    <p>Aenean commodo ligula eget dolor. Aenean massa. Cum sociis natoque penatibus et magnis dis parturient montes, nascetur ridiculus mus. Donec quam felis, ultricies nec, pellentesque eu, pretium quis, sem.</p>
    <a class="btn">Zum Aboshop</a>
  </div>
</section>
<div class="abs magazine" role="img" aria-label="Titelseiten der aktuellen Magazinausgaben"></div>

<!-- Row 4 -->
<article class="abs card" style="left:231px;top:2789px"><div class="media" role="img" aria-label="Foto: Besuchergruppe in einem Büro" style="background:linear-gradient(180deg,#d9dcdc,#8f8d88 55%,#b2403a)"></div><div class="body"><div class="cat">REGIONAL</div><h3>Lorem ipsum dolor sit amet, consectetuer adipiscing elit.</h3><p>Aenean commodo ligula eget dolor. Aenean massa. Cum sociis natoque penatibus et magnis dis parturient montes, nascetur ridiculus... | <span class="more-link">mehr</span></p></div></article>
<article class="abs card" style="left:482px;top:2789px"><div class="media" role="img" aria-label="Foto: Mann im Anzug hinter einer Vitrine mit Uhren" style="background:linear-gradient(180deg,#3a2320,#6a3a2c 50%,#2a1a17)"></div><div class="body"><div class="cat">WIRTSCHAFT</div><h3>Lorem ipsum dolor sit amet, consectetuer adipiscing elit.</h3><p>Aenean commodo ligula eget dolor. Aenean massa. Cum sociis natoque penatibus et magnis dis parturient montes, nascetur ridiculus... | <span class="more-link">mehr</span></p></div></article>
<article class="abs card" style="left:734px;top:2789px"><div class="media" role="img" aria-label="Foto: Golfplatz in hügeliger Landschaft unter blauem Himmel" style="background:linear-gradient(180deg,#3f7dc4,#a9c7e4 35%,#6f9a3a 55%,#8db64a)"></div><div class="body"><div class="cat">SPORT</div><h3>Lorem ipsum dolor sit amet, consectetuer adipiscing elit.</h3><p>Aenean commodo ligula eget dolor. Aenean massa. Cum sociis natoque penatibus et magnis dis parturient montes, nascetur ridiculus... | <span class="more-link">mehr</span></p></div></article>

<footer class="abs footer">
  <div class="rubrics">
    <span>KOMPASSnews</span><span>KOMPASSevents</span><span>KOMPASSjobs</span><span>KOMPASStalk</span><span>KOMPASSfinanzen</span>
    <span>KOMPASSimmobilien</span><span>KOMPASSreisen</span><span>KOMPASShotel</span><span>KOMPASScar</span><span>KOMPASSfamilie</span>
  </div>
  <div class="footlinks">Unternehmen &nbsp;|&nbsp; Partner &nbsp;|&nbsp; Karriere &nbsp;|&nbsp; Kontakt &nbsp;|&nbsp; AGB &nbsp;|&nbsp; Datenschutz &nbsp;|&nbsp; Impressum</div>
  <div class="copyright">© 2018 kompassonline-beispiel.ch</div>
</footer>

</body>
</html>
```